BasinBright Wordpress Design Project

BasinBright is a retrofit for your toilet lid that turns it into a sink. By rerouting clean water from the supply line, BasinBright delivers an automatic, touch-free hand wash with every flush. We already have a wordpress site, but would like to create a "fresh face" for our company, emphasizing the green aspect of our product. Therefore, we want to include both blue and green colors in the design. you can look at our current website here: www.basinbright-example.com. Our old website seems dated and disorganized, we want our new website to be brighter and more inviting.

Target Market(s)

green homeowners, those interested in saving money and resources

Industry/Entity Type

It Company

Requirements
Nice to have
• We want to emphasize the simplicity of our product, and feel that our website should represent that. We would like to have a place for videos, social media links, as well as a menu that has about us/Frequently asked questions/store/etc.

```html
<!DOCTYPE html>
<html lang="en">
<head>
<meta charset="utf-8">
<title>BasinBright – Home</title>
<link href="https://fonts.googleapis.com/css2?family=Ubuntu:ital,wght@0,400;0,500;0,700;1,400&display=swap" rel="stylesheet">
<style>
  :root {
    --page-bg: #ecebe8;
    --charcoal: #3a3a3a;
    --charcoal-deep: #333333;
    --lime: #b4d80c;
    --lime-light: #c6e23a;
    --teal: #93cbb8;
    --teal-light: #c7e6dc;
    --white: #ffffff;
    --ink: #2a2a2a;
  }
  * { box-sizing: border-box; margin: 0; padding: 0; }
  html, body { width: 911px; height: 1200px; overflow: hidden; }
  body {
    position: relative;
    background: var(--page-bg);
    font-family: "Ubuntu", sans-serif;
    color: var(--white);
  }
  .site-header {
    position: absolute; left: 140px; top: 0; width: 634px; height: 130px;
    background: var(--charcoal-deep);
  }
  .brand { position: absolute; left: 4px; top: 48px; }
  .brand-name { font-size: 27px; font-weight: 700; line-height: 1; }
  .brand-tagline { font-size: 11px; line-height: 1.2; }
  .account-links {
    position: absolute; right: 8px; top: 51px; font-size: 12px; word-spacing: 6px;
  }
  .search-box {
    position: absolute; left: 404px; top: 77px; width: 224px; height: 31px;
    border: 1px solid #6a6a6a; background: #444;
    font-size: 13px; font-weight: 700; padding: 8px 0 0 16px;
  }
  .search-box svg { position: absolute; right: 14px; top: 5px; }
  .home-tab {
    position: absolute; left: 140px; top: 123px; width: 58px; height: 20px; background: var(--lime);
  }
  .hero {
    position: absolute; left: 140px; top: 140px; width: 634px; height: 320px;
    background: linear-gradient(90deg, #c6df5a 0%, var(--lime) 45%, #a9d100 100%);
    overflow: hidden;
  }
  .main-nav {
    position: absolute; left: 13px; top: 8px; display: flex; gap: 11px;
    font-size: 12.5px; font-weight: 700; text-transform: uppercase;
  }
  .main-nav .current { color: #5c6b18; }
  .hero-photo {
    position: absolute; left: 0; top: 27px; width: 288px; height: 293px;
    background: radial-gradient(ellipse at 45% 45%, #f4f5f2 0%, #d9ddd6 45%, #b8c68a 80%, #b4d80c 100%);
  }
  .hero-title {
    position: absolute; left: 311px; top: 86px; width: 280px;
    font-size: 23px; font-weight: 500; line-height: 1.2; color: var(--charcoal-deep);
  }
  .hero-text {
    position: absolute; left: 311px; top: 158px; width: 290px;
    font-size: 11px; font-weight: 500; line-height: 1.35; text-transform: uppercase;
  }
  .button {
    position: absolute; background: var(--white); color: var(--ink);
    font-size: 12px; font-weight: 700; text-transform: uppercase;
    display: flex; align-items: center; justify-content: center;
  }
  .hero .button { left: 311px; top: 223px; width: 94px; height: 34px; }
  .pager { position: absolute; left: 524px; top: 296px; display: flex; gap: 6px; }
  .pager span {
    width: 14px; height: 13px; background: var(--white); color: var(--ink);
    font-size: 9px; text-align: center; line-height: 13px; border: 1px solid var(--charcoal);
  }
  .benefits {
    position: absolute; left: 140px; top: 460px; width: 634px; height: 211px; background: var(--teal);
  }
  .benefit { position: absolute; top: 23px; width: 140px; text-align: center; }
  .benefit svg { display: block; margin: 0 auto; }
  .benefit-label {
    margin-top: 7px; font-size: 15px; font-weight: 500; line-height: 1.05; text-transform: uppercase;
  }
  .info-band {
    position: absolute; left: 140px; width: 634px;
  }
  .info-band.dark { top: 671px; height: 216px; background: var(--charcoal); }
  .info-band.teal { top: 887px; height: 217px; background: var(--teal); }
  .column { position: absolute; top: 20px; width: 280px; }
  .column.left { left: 19px; }
  .column.right { left: 344px; }
  .column-title { font-size: 16px; font-weight: 500; text-transform: uppercase; margin-bottom: 23px; }
  .column-text { font-size: 11.3px; line-height: 1.3; }
  .dark .button.left { left: 153px; top: 178px; width: 127px; height: 27px; }
  .dark .button.right { left: 478px; top: 178px; width: 127px; height: 27px; }
  .teal .button.left { left: 153px; top: 178px; width: 127px; height: 27px; }
  .teal .button.right { left: 478px; top: 178px; width: 127px; height: 27px; }
  .testimonial { font-size: 11.3px; font-style: italic; line-height: 1.3; margin-top: -7px; }
  .testimonial-author {
    margin-top: 6px; padding-left: 148px; font-size: 12px; font-weight: 700; font-style: italic;
  }
  .headline { display: flex; gap: 6px; margin-top: -8px; margin-bottom: 12px; }
  .date-badge {
    flex: none; width: 33px; height: 33px; border-radius: 50%; background: var(--charcoal);
    font-size: 11px; font-weight: 700; line-height: 1.1; text-align: center; padding-top: 5px;
  }
  .date-badge small { font-size: 10px; display: block; }
  .headline-title { font-size: 11.3px; font-weight: 500; color: var(--ink); }
  .headline-text { font-size: 11.3px; line-height: 1.25; }
  .signup {
    position: absolute; left: 140px; top: 1123px; width: 343px; height: 47px; background: var(--lime);
  }
  .signup-field {
    position: absolute; left: 19px; top: 15px; width: 183px; height: 23px; background: var(--white);
    color: var(--ink); font-size: 13px; font-weight: 700; text-align: center; line-height: 23px;
  }
  .signup-submit {
    position: absolute; left: 251px; top: 15px; width: 77px; height: 23px; background: var(--charcoal);
    font-size: 13px; font-weight: 700; text-align: center; line-height: 23px;
  }
  .social { position: absolute; left: 690px; top: 1122px; display: flex; gap: 14px; }
  .social span { width: 35px; height: 35px; border-radius: 50%; background: var(--charcoal); }
</style>
</head>
<body>

<header class="site-header">
  <div class="brand">
    <div class="brand-name">BasinBright</div>
    <div class="brand-tagline">The Patented Multipurpose Accesory Sink</div>
  </div>
  <div class="account-links">Register Sign in</div>
  <div class="search-box">SEARCH
    <svg width="26" height="22" viewBox="0 0 26 22" aria-hidden="true">
      <circle cx="10" cy="9" r="6.5" fill="none" stroke="#fff" stroke-width="2.5"/>
      <line x1="15" y1="13" x2="23" y2="19" stroke="#fff" stroke-width="3.5" stroke-linecap="round"/>
    </svg>
  </div>
</header>

<div class="home-tab"></div>

<section class="hero">
  <div class="hero-photo" role="img" aria-label="Product photo: white toilet tank fitted with the sink basin lid and a curved faucet"></div>
  <nav class="main-nav">
    <span class="current">Home</span><span>About Us</span><span>Benefits</span><span>FAQs</span><span>Partners</span><span>Retailers Program</span><span>Store</span><span>News</span><span>Contact</span>
  </nav>
  <h1 class="hero-title">THE PROOF IS IN THE POSITIVES</h1>
  <p class="hero-text">Lorem ipsum dolor sit amet,consectetur adipiscing elit,sed do eusmod tempor insididunt ut labore et dalore magna aliqua.</p>
  <a class="button">Read More</a>
  <div class="pager"><span>1</span><span>2</span><span>3</span></div>
</section>

<section class="benefits">
  <div class="benefit" style="left:19px">
    <svg width="118" height="118" viewBox="0 0 118 118" role="img" aria-label="Water icon">
      <circle cx="59" cy="59" r="55" fill="var(--teal-light)"/>
      <circle cx="59" cy="59" r="45" fill="#fff"/>
      <path d="M59 24 C50 40 40 52 40 66 a19 19 0 0 0 38 0 C78 52 68 40 59 24Z" fill="var(--teal)"/>
    </svg>
    <div class="benefit-label">Conserves<br>Water</div>
  </div>
  <div class="benefit" style="left:135px">
    <svg width="118" height="118" viewBox="0 0 118 118" role="img" aria-label="Savings icon">
      <circle cx="59" cy="59" r="55" fill="var(--teal-light)"/>
      <circle cx="59" cy="59" r="45" fill="var(--teal)"/>
      <circle cx="59" cy="59" r="26" fill="#fff"/>
    </svg>
    <div class="benefit-label">Saves<br>Money</div>
  </div>
  <div class="benefit" style="left:257px">
    <svg width="118" height="118" viewBox="0 0 118 118" role="img" aria-label="Water drop over open hand icon">
      <circle cx="59" cy="59" r="55" fill="var(--teal-light)"/>
      <circle cx="59" cy="59" r="45" fill="var(--teal)"/>
      <path d="M59 30 C53 41 48 48 48 55 a11 11 0 0 0 22 0 C70 48 65 41 59 30Z" fill="#fff"/>
      <rect x="36" y="72" width="46" height="9" rx="4.5" fill="#fff"/>
    </svg>
    <div class="benefit-label">Manages<br>Small Spaces</div>
  </div>
  <div class="benefit" style="left:378px">
    <svg width="118" height="118" viewBox="0 0 118 118" role="img" aria-label="Drop icon">
      <circle cx="59" cy="59" r="55" fill="var(--teal-light)"/>
      <circle cx="59" cy="59" r="45" fill="#fff"/>
      <path d="M59 22 C49 40 38 52 38 68 a21 21 0 0 0 42 0 C80 52 69 40 59 22Z" fill="var(--teal)"/>
    </svg>
    <div class="benefit-label">Promotes<br>Hygeine &amp;<br>Sanitation</div>
  </div>
  <div class="benefit" style="left:501px">
    <svg width="118" height="118" viewBox="0 0 118 118" role="img" aria-label="Family icon">
      <circle cx="59" cy="59" r="55" fill="var(--teal-light)"/>
      <circle cx="59" cy="59" r="45" fill="var(--teal)"/>
    </svg>
    <div class="benefit-label">Engages<br>All Ages</div>
  </div>
</section>

<section class="info-band dark">
  <div class="column left">
    <h2 class="column-title">Where to Buy?</h2>
    <p class="column-text">BasinBright is available at retail outlets that offer cost-saving and environmentally sustainable options in the household products space. Our exclusive retail network is expanding throughout the United States and abroad, including these key online and traditional retailers:</p>
  </div>
  <div class="column right">
    <h2 class="column-title">Verdant Design Studio</h2>
    <p class="column-text">Verdant Design Studio, LLC is an Industrial Design firm dedicated to socially-conscious and environmentally responsible products that add to consumers' quality of life. As the manufacturers of BasinBright, we're doing what we can to reduce the worldwide demand on water, and the energy and other resources required to move it.</p>
  </div>
  <a class="button left">Leafline Goods</a>
  <a class="button right">Read More</a>
</section>

<section class="info-band teal">
  <div class="column left">
    <h2 class="column-title">Client Testimonials</h2>
    <p class="testimonial">“Sed ut perspiciatis unde omnis iste natus error sit voluptatem accusantium doloremque laudantium, totam rem aperiam, eaque ipsa quae ab illo inventore veritatis et quasi architecto beatae vitae dicta sunt explicabo.”</p>
    <p class="testimonial-author">J. Mercer</p>
  </div>
  <div class="column right">
    <h2 class="column-title">Recent Headlines</h2>
    <div class="headline">
      <div class="date-badge">17th<small>Sept</small></div>
      <div><div class="headline-title">At vero eos et accusamus</div>
      <div class="headline-text">Lorem ipsum dolor sit amet, consectetur adipisicing elit, sed do eiusmod tempor</div></div>
    </div>
    <div class="headline">
      <div class="date-badge">20th<small>Sept</small></div>
      <div><div class="headline-title">At vero eos et accusamus</div>
      <div class="headline-text">Lorem ipsum dolor sit amet, consectetur adipisicing elit, sed do eiusmod tempor</div></div>
    </div>
  </div>
  <a class="button left">Read More</a>
  <a class="button right">Read More</a>
</section>

<footer>
  <div class="signup">
    <div class="signup-field">YOUR EMAIL ADDRESS</div>
    <div class="signup-submit">SUBMIT</div>
  </div>
  <div class="social">
    <span role="img" aria-label="Social network link"></span>
    <span role="img" aria-label="Social network link"></span>
  </div>
</footer>

</body>
</html>
```